Innovative global company needs a design for an attractive customer business quote

We need a design for a business quote which is a written offer from a seller to a prospective buyer. Business quotes are often a key step in the complex sales process.

Our company brings human insight to business by studying how people work, wherever they work. Those insights can help organizations achieve a higher level of performance, by creating places that unlock the promise of their people. We are a global, publicly traded company.

Guidelines:
Version 1: Use all the data from the example to product an attractive looking quote using every bit of detail. It should clearly explain to a customer what there order will look like.
Version 2: Use a subset of the data (highlighted on second document) to product a leaner/cleaner looking quote.

• All versions need to use the product illustrations for a quick visual reference to the reader (in zip file, image files named by catalog number).
• The output should be scalable to US Letter and European A4
• The quote should look professional but not stuffy.
• Color is OK to use (no red)
• Make sure you leave space for a logo, along with company information.
• Should be light and airy with white space
Updates

The design needs to be creative and unique. We are ok with it being drastically different as long as it has the content.

I want 2 versions, one with all the data and the other with just the text highlighted in yellow.
I want this quote to be readable and easy for customers to understand.
the vertical lines are not required, in fact it would be nice to see a design without those vertical lines

Industry/Entity Type

Business

Font styles to use
Sans Serif

Requirements
Must have
• 2 versions submitted:
One is with all the data
Second is the subset of the data (note the highlighted text).

Both version must have Art.

```html
<!DOCTYPE html>
<html lang="en">
<head>
<meta charset="utf-8">
<title>Quotation 2327</title>
<link href="https://fonts.googleapis.com/css2?family=Open+Sans:wght@400;600;700&display=swap" rel="stylesheet">
<style>
:root{
  --ink:#1f2430;
  --muted:#6b7283;
  --navy:#4a5578;
  --navy-soft:#eef0f6;
  --line:#d9dce4;
  --chip:#e6e8ef;
  --paper:#ffffff;
  --art-a:#f1f2f5;
  --art-b:#dfe2e8;
}
*{margin:0;padding:0;box-sizing:border-box}
html,body{width:927px;height:1200px;overflow:hidden;background:var(--paper)}
body{font-family:"Open Sans",Arial,sans-serif;color:var(--ink);font-size:14px;line-height:1.45}
.page{position:relative;width:927px;height:1200px;padding:40px 48px}

.masthead{display:flex;justify-content:space-between;align-items:flex-start;height:70px}
.brand{display:flex;align-items:center;gap:12px}
.brand-mark{width:26px;height:26px;background:var(--navy)}
.brand-name{font-size:20px;font-weight:700;color:var(--ink)}
.brand-info{margin-top:6px;font-size:12px;color:var(--muted)}
.doc-title{text-align:right}
.doc-title h1{font-size:30px;font-weight:700;letter-spacing:3px;color:var(--navy);line-height:1.1}
.doc-title p{font-size:12px;color:var(--muted);margin-top:4px;letter-spacing:1px}
.accent{height:3px;width:64px;background:var(--navy);margin:16px 0 22px}

.meta{display:grid;grid-template-columns:repeat(6,auto);justify-content:space-between;background:var(--navy-soft);border-radius:8px;padding:16px 22px}
.meta dt{font-size:10.5px;font-weight:600;letter-spacing:.8px;text-transform:uppercase;color:var(--muted)}
.meta dd{font-size:15px;font-weight:600;margin-top:2px}

.parties{display:grid;grid-template-columns:1fr 1fr 180px;gap:24px;margin-top:28px}
.label{font-size:10.5px;font-weight:700;letter-spacing:.8px;text-transform:uppercase;color:var(--navy);margin-bottom:6px}
.parties address{font-style:normal;font-size:14px;line-height:1.5}
.terms-value{font-size:14px;font-weight:600}

.items-head{display:grid;grid-template-columns:44px 140px 1fr 60px 90px 100px;column-gap:14px;margin-top:34px;padding-bottom:8px;border-bottom:2px solid var(--navy)}
.items-head span{font-size:10.5px;font-weight:700;letter-spacing:.8px;text-transform:uppercase;color:var(--muted)}
.num{text-align:right}

.item{display:grid;grid-template-columns:44px 140px 1fr 60px 90px 100px;column-gap:14px;padding:22px 0;border-bottom:1px solid var(--line)}
.line-no{width:30px;height:30px;border-radius:50%;background:var(--navy);color:#fff;font-weight:700;font-size:13px;display:flex;align-items:center;justify-content:center}
.art{width:140px;height:140px;border-radius:8px;background:linear-gradient(160deg,var(--art-a),var(--art-b))}
.item h2{font-size:15.5px;font-weight:700;line-height:1.35}
.spec{display:grid;grid-template-columns:78px 1fr;margin-top:10px;font-size:13px}
.spec dt{color:var(--muted);font-weight:600;font-size:11px;letter-spacing:.6px;line-height:20px}
.spec dd{line-height:20px}
.options{margin-top:12px}
.options .label{margin-bottom:6px}
.chips{list-style:none;display:flex;flex-wrap:wrap;gap:6px}
.chips li{background:var(--chip);border-radius:12px;padding:2px 10px;font-size:11.5px;font-weight:600;color:var(--ink)}
.figure{font-size:15px;text-align:right;padding-top:4px}
.figure.amount{font-weight:700;color:var(--navy)}
</style>
</head>
<body>
<main class="page">
  <header class="masthead">
    <div>
      <div class="brand"><div class="brand-mark"></div><div class="brand-name">Halden Workplace</div></div>
      <p class="brand-info">410 Carver Street, Holland, MI 49423 &middot; (616) 555-0142</p>
    </div>
    <div class="doc-title"><h1>QUOTATION</h1><p>PAGE 1/3</p></div>
  </header>
  <div class="accent"></div>

  <dl class="meta">
    <div><dt>Quote number</dt><dd>2327</dd></div>
    <div><dt>Quote date</dt><dd>4/10/2014</dd></div>
    <div><dt>Customer order no.</dt><dd>1467942</dd></div>
    <div><dt>Customer no.</dt><dd>35</dd></div>
    <div><dt>Account rep.</dt><dd>Dana Morrow</dd></div>
    <div><dt>Project ID</dt><dd>abc1</dd></div>
  </dl>

  <section class="parties">
    <div><p class="label">Quote to</p><address>Northfield Company<br>2240 Lakeview Ave<br>Fairhaven, MI 49302</address></div>
    <div><p class="label">Ship to</p><address>Northfield Company<br>2240 Lakeview Ave<br>Fairhaven, MI 49302</address></div>
    <div><p class="label">Terms</p><p class="terms-value">Due Upon Receipt</p></div>
  </section>

  <div class="items-head">
    <span>Line</span><span>Item</span><span>Model Number/Description</span><span class="num">Qty</span><span class="num">Unit Price</span><span class="num">Extended</span>
  </div>

  <article class="item">
    <div class="line-no">1</div>
    <div class="art" role="img" aria-label="Product illustration: freestanding corner desk"></div>
    <div>
      <h2>Meridian freestanding; Desk-Corner, 24D x 36W</h2>
      <dl class="spec"><dt>BASIC</dt><dd>Mist</dd><dt>EDGE</dt><dd>Black</dd><dt>TOP SURF</dt><dd>Black</dd></dl>
      <div class="options"><p class="label">Options</p>
        <ul class="chips"><li>SCALLOPS</li><li>3 CORNER SUPPORTS</li><li>HALF HEIGHT MODESTY PANEL</li></ul>
      </div>
    </div>
    <div class="figure">5</div>
    <div class="figure">850</div>
    <div class="figure amount">850</div>
  </article>

  <article class="item">
    <div class="line-no">2</div>
    <div class="art" role="img" aria-label="Product illustration: tall storage tower with hinged door"></div>
    <div>
      <h2>Tower, door hinged left hand with drawers, 24D x 15 1/2W x 72 5/8H</h2>
      <dl class="spec"><dt>BASIC</dt><dd>Black</dd><dt>FRONT</dt><dd>Black</dd><dt>LOCK</dt><dd>Ember Chrome</dd></dl>
      <div class="options"><p class="label">Options</p>
        <ul class="chips"><li>GLS DOOR</li><li>ICE WHITE</li><li>BAR PULL</li></ul>
      </div>
    </div>
    <div class="figure">2</div>
    <div class="figure">825</div>
    <div class="figure amount">825</div>
  </article>
</main>
</body>
</html>
```